Simple, Professional and neat business card design for Vendralo Inc.

We're looking to re-vamp our business card design. We're a supplier of innovative feed ingredients for the North American animal agriculture industry. We are located in Lucknow, Ontario, Canada and our flagship product is a product that prevents milk fever in dairy cows when the calve, it is fed before calving and is very effective compared to other alternatives available on the market today.

Our company has Danish roots and we import all of our product from our Danish partner/manufacturer in Denmark. We like our design to embrace high professionalism while remaining neat and simple.

Target Market(s)

B2B, Feed Mills, Veterinary Clinics, Large integrators/producers,

Industry/Entity Type

Agribusiness

Contact Information for Business Card

We like the rounded corners because they make the card easy to sit in a wallet and not many use it so it makes the card stand out, just possibly something to take account for during the design.

As you can also see on the sliders below, looking for a that simple but proffesional scandinavian design.

Requirements
Nice to have
• Rounded corners
Should not have
• Too vibrant

```html
<!DOCTYPE html>
<html lang="en">
<head>
<meta charset="utf-8">
<title>Vendralo Inc. – Business Card</title>
<link rel="stylesheet" href="https://fonts.googleapis.com/css2?family=Open+Sans:wght@400;600;700;800&display=swap">
<style>
  :root {
    --brand-blue: #1d5aa8;
    --brand-blue-dark: #154a8f;
    --brand-blue-deep: #0f3d7a;
    --paper: #ffffff;
    --backdrop: #e4e1dc;
    --divider: #2b2b2b;
    --ink-light: #ffffff;
  }
  * { box-sizing: border-box; margin: 0; padding: 0; }
  html, body { width: 1200px; height: 962px; overflow: hidden; }
  body {
    background: var(--backdrop);
    font-family: "Open Sans", Arial, sans-serif;
    position: relative;
  }
  .card {
    position: absolute;
    left: 220px;
    width: 760px;
    height: 430px;
    background: var(--paper);
    border-radius: 22px;
    overflow: hidden;
    box-shadow: 0 4px 14px rgba(0,0,0,0.18);
  }
  .card--front { top: 30px; }
  .card--back { top: 502px; }

  /* Wordmark */
  .wordmark {
    display: flex;
    align-items: center;
    gap: 22px;
    color: var(--brand-blue);
    font-weight: 800;
    font-size: 50px;
    letter-spacing: 0.5px;
  }
  .wordmark__mark {
    width: 62px; height: 62px;
    background: var(--brand-blue);
    border-radius: 6px;
  }

  /* Front */
  .card--front .wordmark { position: absolute; top: 36px; left: 190px; }
  .tagline-band {
    position: absolute; top: 138px; left: 0; right: 0;
    height: 60px;
    background: var(--brand-blue);
    color: var(--ink-light);
    font-weight: 600;
    font-size: 16px;
    line-height: 20px;
    text-align: center;
    padding-top: 10px;
  }
  .features {
    position: absolute; top: 198px; left: 0; right: 0; bottom: 0;
    display: grid;
    grid-template-columns: 1fr 1fr 1fr;
  }
  .feature {
    display: flex; flex-direction: column; align-items: center;
    justify-content: center; gap: 14px;
    color: var(--brand-blue);
    font-weight: 600;
    font-size: 17px;
  }
  .feature + .feature { border-left: 3px solid var(--divider); }
  .feature svg { width: 104px; height: 104px; }

  /* Back */
  .card--back .wordmark { position: absolute; top: 28px; left: 240px; }
  .back-panel {
    position: absolute; top: 130px; left: 0; right: 0; bottom: 0;
    background: var(--brand-blue);
    color: var(--ink-light);
  }
  .contact-person {
    position: absolute; top: 24px; left: 52px;
  }
  .contact-person__name {
    font-weight: 700; font-size: 30px; margin-bottom: 10px;
  }
  .contact-line {
    display: flex; align-items: center; gap: 10px;
    font-size: 20px; line-height: 32px;
  }
  .contact-line svg { width: 18px; height: 18px; }
  .phones {
    position: absolute; top: 90px; right: 70px;
    list-style: none;
  }
  .phones li {
    display: flex; align-items: center; gap: 14px;
    font-size: 21px; line-height: 36px;
  }
  .phones .icon-tile {
    width: 24px; height: 24px; background: var(--ink-light);
    border-radius: 4px; display: flex; align-items: center; justify-content: center;
  }
  .phones svg { width: 16px; height: 16px; }
  .address-band {
    position: absolute; left: 0; right: 0; bottom: 0;
    height: 64px;
    background: var(--brand-blue-deep);
    display: flex; align-items: center; gap: 14px;
    padding-left: 52px;
    font-size: 22px;
  }
  .address-band svg { width: 26px; height: 26px; }
</style>
</head>
<body>

<section class="card card--front" aria-label="Business card front">
  <div class="wordmark"><span class="wordmark__mark"></span><span>VENDRALO INC.</span></div>
  <div class="tagline-band">Distributor Of Innovation Feed Ingredients<br>And Other Preventative Health Products</div>
  <div class="features">
    <div class="feature">
      <svg viewBox="0 0 100 100" fill="none" stroke="var(--brand-blue)" stroke-width="6" stroke-linejoin="round">
        <path d="M50 6 C64 16 78 18 90 16 C90 56 76 80 50 94 C24 80 10 56 10 16 C22 18 36 16 50 6 Z"/>
        <circle cx="50" cy="48" r="16" fill="var(--brand-blue)" stroke="none"/>
        <path d="M50 40 V56 M42 48 H58" stroke="#fff" stroke-width="4"/>
      </svg>
      <span>Preventative Care</span>
    </div>
    <div class="feature">
      <svg viewBox="0 0 100 100" fill="none" stroke="var(--brand-blue)" stroke-width="6" stroke-linecap="round">
        <path d="M20 78 A40 40 0 1 1 88 56"/>
        <path d="M50 50 L64 22" stroke-width="7"/>
        <path d="M22 90 L44 70 L56 80 L90 52"/>
        <path d="M76 50 H92 V66"/>
      </svg>
      <span>High- performance</span>
    </div>
    <div class="feature">
      <svg viewBox="0 0 100 100" fill="none" stroke="var(--brand-blue)" stroke-width="7">
        <circle cx="50" cy="50" r="42"/>
        <text x="50" y="66" text-anchor="middle" font-family="Georgia, serif" font-size="42" font-weight="700" fill="var(--brand-blue)" stroke="none">Rx</text>
        <path d="M20 80 L80 20"/>
      </svg>
      <span>Prescription- free</span>
    </div>
  </div>
</section>

<section class="card card--back" aria-label="Business card back">
  <div class="wordmark"><span class="wordmark__mark"></span><span>VENDRALO INC.</span></div>
  <div class="back-panel">
    <div class="contact-person">
      <p class="contact-person__name">Mikkel Brandt</p>
      <p class="contact-line">
        <svg viewBox="0 0 20 20" fill="none" stroke="#fff" stroke-width="2"><circle cx="10" cy="10" r="4"/><path d="M14 10 v2 a3 3 0 0 0 5 -2 a9 9 0 1 0 -4 7.5"/></svg>
        mikkel@vendralo.com
      </p>
      <p class="contact-line">
        <svg viewBox="0 0 20 20" fill="none" stroke="#fff" stroke-width="1.6"><circle cx="10" cy="10" r="8.5"/><ellipse cx="10" cy="10" rx="4" ry="8.5"/><path d="M1.5 10 H18.5 M3 5.5 H17 M3 14.5 H17"/></svg>
        www.vendralo.com
      </p>
    </div>
    <ul class="phones">
      <li><span class="icon-tile"><svg viewBox="0 0 16 16" fill="var(--brand-blue)"><rect x="4" y="1" width="8" height="14" rx="1.5"/><rect x="5.5" y="3" width="5" height="8" fill="#fff"/></svg></span>555-210-0417</li>
      <li><span class="icon-tile"><svg viewBox="0 0 16 16" fill="var(--brand-blue)"><path d="M3 1 L6 1 L7 5 L5 6.5 C6 9 7 10 9.5 11 L11 9 L15 10 L15 13 C15 14 14 15 13 15 C6 15 1 10 1 3 C1 2 2 1 3 1 Z"/></svg></span>555-210-0488</li>
      <li><span class="icon-tile"><svg viewBox="0 0 16 16" fill="none" stroke="var(--brand-blue)" stroke-width="1.8"><circle cx="8" cy="8" r="6.5"/><path d="M5 8 H11 M8 5 V11"/></svg></span>800-555-0162</li>
      <li><span class="icon-tile"><svg viewBox="0 0 16 16" fill="var(--brand-blue)"><rect x="4" y="1" width="8" height="4"/><rect x="1" y="6" width="14" height="6" rx="1"/><rect x="4" y="10" width="8" height="5" fill="#fff" stroke="var(--brand-blue)" stroke-width="1.2"/></svg></span>555-210-0499</li>
    </ul>
    <div class="address-band">
      <svg viewBox="0 0 26 26" fill="#fff"><path d="M13 2 L25 13 H21 V24 H15 V17 H11 V24 H5 V13 H1 Z"/></svg>
      <span>Box 407, Lakeview, Ontario Canada N0X 1A0</span>
    </div>
  </div>
</section>

</body>
</html>
```